MORVAL infographic (architecture design and basic content)

We would like an infographic that will include the content found in the attached pptx file and in the attached image. On the top of the infographic we would like the content of the powerpoint presentation and in the bottom we would like a redesign of the attached figure. The figure should have the color patterns of the project (see logo). It is important to have a nice redesign of the attached architecture (figure).

Target Market(s)

Policy Makers

Font styles to use
Sans Serif

Colors
33b8a4

Requirements
Must have
• The project must have the following scale:
• - 16:18 The content of the ppt should be placed on top (16:9) and the architecture (figure) should be placed at the bottom (16:9).
Nice to have
• I also attach the project's brochure which was designed a couple of months ago. This is just to showcase the colors etc. that we would like.

```html
<!DOCTYPE html>
<html lang="en">
<head>
<meta charset="utf-8">
<title>MORVAL – Universal Cybersecurity Toolkit</title>
<link rel="stylesheet" href="https://fonts.googleapis.com/css2?family=Questrial&family=Ubuntu:wght@400;700&family=Open+Sans:wght@400;600;700&display=swap">
<style>
  :root{
    --teal:#33b8a4;
    --teal-deep:#1e9c8c;
    --teal-dark:#17756a;
    --teal-soft:#6ab9b1;
    --teal-pale:#9ccfd0;
    --teal-mid:#67b5b0;
    --grey-panel:#a0a4a8;
    --band:#e3e6ea;
    --panel:#f2f2f2;
    --ink:#222;
    --white:#fff;
  }
  *{box-sizing:border-box;margin:0;padding:0}
  html,body{width:1200px;height:729px;overflow:hidden;background:var(--white)}
  body{position:relative;font-family:"Questrial",sans-serif;color:var(--ink)}
  .abs{position:absolute}

  .sheet{position:absolute;left:101px;top:49px;width:1002px;height:612px;background:var(--white);box-shadow:0 6px 18px rgba(0,0,0,.12)}
  .top-band{left:101px;top:49px;width:1002px;height:197px;background:linear-gradient(180deg,#dfe3e8,#e6e9ec)}

  .brand{left:145px;top:109px;width:180px;display:flex;align-items:center;gap:8px;white-space:nowrap}
  .brand-dot{flex:none;width:46px;height:46px;border-radius:50%;border:3px solid var(--teal)}
  .brand-name{font-family:"Ubuntu",sans-serif;font-weight:400;font-size:29px;line-height:1;color:var(--teal)}
  .tagline{left:148px;top:163px;width:180px;font-family:"Ubuntu",sans-serif;font-size:13.5px;line-height:20px;color:var(--teal);white-space:nowrap}
  .tagline b{font-weight:700}
  .tagline .strong-line{letter-spacing:.8px}

  .panel{top:138px;height:108px}
  .panel-goals{left:331px;width:227px;background:var(--teal-pale)}
  .panel-objectives{left:563px;width:298px;background:var(--teal-mid)}
  .panel-pilots{left:865px;width:238px;background:var(--grey-panel)}

  .tab{top:111px;height:38px;border-radius:19px;background:linear-gradient(180deg,#eef0f2,#e4e7ea);border:1px dotted var(--teal);box-shadow:0 3px 6px rgba(0,0,0,.08);font-family:"Open Sans",sans-serif;font-size:22px;line-height:1;letter-spacing:3px;color:var(--teal);padding:9px 0 0 22px;white-space:nowrap}
  .tab-goals{left:335px;width:217px}
  .tab-objectives{left:577px;width:217px;padding-left:15px}
  .tab-pilots{left:874px;width:217px;padding-left:23px}

  .goals-text{left:358px;top:166px;width:187px;font-size:8.6px;line-height:10.6px;color:var(--white);text-align:justify}
  .bullets{list-style:none;color:var(--white);font-size:9px;line-height:10.5px}
  .bullets li{position:relative;padding-left:11px}
  .bullets li::before{content:"";position:absolute;left:0;top:3px;border-left:3px solid transparent;border-right:3px solid transparent;border-top:4px solid var(--white)}
  .objectives-list{left:569px;top:168px;width:290px}
  .pilots-list{left:886px;top:167px;width:215px;font-size:10px;line-height:11.5px}

  .map-area{left:101px;top:280px;width:290px;height:381px;background:radial-gradient(ellipse at 45% 45%,#e4e4e4 0%,#ececec 45%,#fafafa 80%)}
  .kb-panel{left:391px;top:253px;width:417px;height:367px;background:var(--panel)}
  .sb-panel{left:817px;top:253px;width:286px;height:367px;background:var(--panel)}
  .platform{left:391px;top:619px;width:712px;height:42px;background:var(--teal-soft);color:var(--white);font-family:"Open Sans",sans-serif;font-weight:600;font-size:15.5px;letter-spacing:2.4px;text-align:center;line-height:42px}

  .diagram{left:0;top:0;width:1200px;height:729px}

  .node{border-radius:50%;background:#f7f7f7;border:2px solid #555;box-shadow:0 4px 12px rgba(0,0,0,.25);display:flex;flex-direction:column;align-items:center;justify-content:center;text-align:center}
  .node-core{left:348px;top:360px;width:98px;height:98px;font-family:"Ubuntu",sans-serif;color:var(--teal);font-size:14px;letter-spacing:1px}
  .node-toolbox{left:199px;top:372px;width:74px;height:74px;font-family:"Open Sans",sans-serif;font-size:7.4px;line-height:9px;color:var(--teal);letter-spacing:.5px}
  .node-api{left:220px;top:463px;width:63px;height:63px}
  .node-label{font-family:"Open Sans",sans-serif;font-size:8px;line-height:10px;letter-spacing:.6px;color:var(--ink);text-align:center}

  .pill{height:18px;border-radius:9px;background:linear-gradient(90deg,var(--teal) 0%,#6fbfb1 100%);box-shadow:2px 3px 5px rgba(0,0,0,.25);color:var(--white);font-size:10px;line-height:18px;padding-left:24px;white-space:nowrap}
  .pill::before{content:"";position:absolute;left:5px;top:4px;width:8px;height:8px;border-radius:50%;border:1.5px solid var(--white)}

  .dotbox{border:1px dotted var(--teal);border-radius:4px}
  .feature{font-size:9px;line-height:9px;color:var(--ink)}
  .feature p+p{margin-top:6px}

  .section-title{font-family:"Open Sans",sans-serif;font-weight:700;font-size:15.5px;letter-spacing:2.2px;color:var(--teal-soft)}

  .sb-box{left:884px;width:132px;height:44px;display:flex;align-items:center;justify-content:center;text-align:center;font-family:"Open Sans",sans-serif;font-size:7.8px;line-height:10.5px;letter-spacing:.7px}
  .sb-outline{border:1px dotted var(--teal);border-radius:4px;color:var(--ink)}
  .sb-filled{background:linear-gradient(90deg,var(--teal),#70bba9);color:var(--white);border-radius:3px;box-shadow:0 2px 4px rgba(0,0,0,.15)}
  .sandbox-frame{left:879px;top:417px;width:142px;height:72px;border:1px dotted var(--teal);border-radius:4px}
  .sandbox-word{left:879px;top:470px;width:142px;text-align:center;font-family:"Open Sans",sans-serif;font-weight:600;font-size:11.5px;letter-spacing:1.4px;color:var(--teal-soft)}
  .sandbox-env{left:860px;top:578px;width:190px;text-align:center;font-family:"Open Sans",sans-serif;font-size:11.5px;line-height:15px;letter-spacing:1.3px;color:var(--teal-soft)}
  .sandbox-env b{font-weight:700}
</style>
</head>
<body>
  <div class="sheet"></div>

  <!-- Header band -->
  <div class="abs top-band"></div>
  <div class="abs brand"><span class="brand-dot"></span><span class="brand-name">MORVAL</span></div>
  <div class="abs tagline">A Universal <b>Cybersecurity</b><br>Toolkit for the<br><b class="strong-line">Healthcare Industry</b></div>

  <div class="abs panel panel-goals"></div>
  <div class="abs panel panel-objectives"></div>
  <div class="abs panel panel-pilots"></div>

  <svg class="abs" style="left:0;top:0" width="1200" height="160">
    <line x1="552" y1="130" x2="577" y2="130" stroke="#33b8a4" stroke-width="1" stroke-dasharray="1.5 1.5"/>
    <line x1="794" y1="130" x2="874" y2="130" stroke="#33b8a4" stroke-width="1" stroke-dasharray="1.5 1.5"/>
  </svg>

  <div class="abs tab tab-goals">Goals</div>
  <div class="abs tab tab-objectives">Objectives</div>
  <div class="abs tab tab-pilots">Pilots</div>

  <p class="abs goals-text">MORVAL aims to introduce a health tailored Universal Cybersecurity Toolkit, thus enhancing the cyber protection of the Health and care IT Ecosystem and ensuring patient data privacy and integrity.</p>

  <ul class="abs bullets objectives-list">
    <li>Cyber protection and data privacy and integrity</li>
    <li>Proactive assessment and mitigation of Cybersecurity threats</li>
    <li>Evaluation and verification of new Medical Devices &amp; Services</li>
    <li>Provision of the MORVAL Certification</li>
    <li>Near real-time vulnerability assessment of operating<br>IT Ecosystems</li>
  </ul>

  <ul class="abs bullets pilots-list">
    <li>Greece: Aegean University Hospital,</li>
    <li>the Thessaly General Hospital</li>
    <li>Spain: The Hospital Santa Clara Verde</li>
    <li>Portugal: the Lumena Medical Clinic</li>
  </ul>

  <!-- Architecture -->
  <div class="abs map-area" role="img" aria-label="Soft grey world map of the Americas behind the toolkit nodes"></div>
  <div class="abs kb-panel"></div>
  <div class="abs sb-panel"></div>

  <svg class="abs diagram" width="1200" height="729">
    <defs>
      <clipPath id="kb-clip"><rect x="391" y="253" width="417" height="367"/></clipPath>
    </defs>
    <circle cx="397" cy="409" r="113" fill="#bfe0dd" fill-opacity=".55" stroke="#9aa" stroke-width=".6" clip-path="url(#kb-clip)"/>
    <path d="M399 343 A68 68 0 0 1 465 400" fill="none" stroke="#17756a" stroke-width="3.5"/>
    <path d="M465 400 A68 68 0 0 1 399 477" fill="none" stroke="#33b8a4" stroke-width="3.5"/>
    <g fill="none" stroke="#33b8a4" stroke-width="1" stroke-dasharray="1.5 1.5">
      <line x1="273" y1="409" x2="343" y2="409"/>
      <polyline points="268,467 302,440 354,440"/>
      <line x1="399" y1="306" x2="399" y2="343"/>
      <line x1="399" y1="477" x2="399" y2="516"/>
      <line x1="447" y1="366" x2="485" y2="340"/>
      <line x1="465" y1="410" x2="509" y2="410"/>
      <line x1="447" y1="458" x2="480" y2="485"/>
      <line x1="608" y1="340" x2="627" y2="340"/>
      <line x1="624" y1="410" x2="645" y2="410"/>
      <line x1="587" y1="486" x2="609" y2="486"/>
      <line x1="750" y1="428" x2="879" y2="428"/>
    </g>
    <g fill="#33b8a4">
      <circle cx="273" cy="409" r="3"/><circle cx="343" cy="409" r="3"/>
      <circle cx="268" cy="467" r="3"/><circle cx="229" cy="520" r="3"/>
      <circle cx="354" cy="440" r="3"/><circle cx="750" cy="428" r="3"/>
    </g>
  </svg>

  <div class="abs node node-core">MORVAL</div>
  <div class="abs node node-toolbox">
    <svg width="22" height="22" viewBox="0 0 22 22" aria-hidden="true">
      <rect x="6" y="10" width="10" height="8" rx="1.5" fill="#33b8a4"/>
      <path d="M8 10V7a3 3 0 0 1 6 0v3" fill="none" stroke="#33b8a4" stroke-width="1.6"/>
    </svg>
    <span>Cyber Security<br>Toolbox</span>
  </div>
  <div class="abs node node-api">
    <svg width="38" height="38" viewBox="0 0 38 38" aria-hidden="true">
      <g fill="#1e9c8c" transform="translate(19 19)">
        <rect x="-3.5" y="-18" width="7" height="8" rx="1"/><rect x="-3.5" y="10" width="7" height="8" rx="1"/>
        <rect x="-18" y="-3.5" width="8" height="7" rx="1"/><rect x="10" y="-3.5" width="8" height="7" rx="1"/>
        <g transform="rotate(45)"><rect x="-3.5" y="-18" width="7" height="8" rx="1"/><rect x="-3.5" y="10" width="7" height="8" rx="1"/><rect x="-18" y="-3.5" width="8" height="7" rx="1"/><rect x="10" y="-3.5" width="8" height="7" rx="1"/></g>
      </g>
      <circle cx="19" cy="19" r="11.5" fill="none" stroke="#1e9c8c" stroke-width="6"/>
    </svg>
  </div>
  <div class="abs node-label" style="left:308px;top:451px">MORVAL<br>Cyber Security</div>
  <div class="abs node-label" style="left:170px;top:526px;text-align:right">Third party<br>&nbsp;&nbsp;&nbsp;&nbsp;&nbsp;&nbsp;&nbsp;&nbsp;API</div>

  <!-- Knowledge base rows -->
  <div class="abs dotbox" style="left:391px;top:279px;width:252px;height:39px"></div>
  <div class="abs pill" style="left:393px;top:290px;width:110px">Decision support</div>
  <div class="abs feature" style="left:526px;top:293px;line-height:10px">Analytic Engine<br>Interactive Dashboard</div>

  <div class="abs dotbox" style="left:627px;top:331px;width:105px;height:55px"></div>
  <div class="abs pill" style="left:480px;top:332px;width:128px">Data traffice monitor</div>
  <div class="abs feature" style="left:636px;top:341px"><p>Anomaly Detection</p><p style="margin-top:9px">Security Protocol<br>Analysis</p></div>

  <div class="abs dotbox" style="left:645px;top:401px;width:105px;height:54px"></div>
  <div class="abs pill" style="left:505px;top:402px;width:119px">Security Information</div>
  <div class="abs feature" style="left:656px;top:406px"><p>Forensics Data<br>Collection Engine</p><p>Blackchain Based<br>Threat Registry</p></div>

  <div class="abs dotbox" style="left:609px;top:476px;width:117px;height:54px"></div>
  <div class="abs pill" style="left:476px;top:477px;width:111px">AI Honeypot</div>
  <div class="abs feature" style="left:619px;top:483px"><p>Machine Learning<br>Intrusion Detection</p><p style="margin-top:7px">Real-time Cyber<br>Risk Assessment</p></div>

  <div class="abs dotbox" style="left:391px;top:511px;width:161px;height:54px"></div>
  <div class="abs pill" style="left:394px;top:516px;width:149px">Homomorphic Encryption</div>
  <div class="abs feature" style="left:413px;top:542px">Anonymisation and<br>privacy</div>
  <div class="abs feature" style="left:413px;top:568px;font-size:10px">Vulnerability<br>Assessment as a<br>Service</div>

  <div class="abs section-title" style="left:524px;top:590px">Knowledge Base</div>

  <!-- Sandbox -->
  <div class="abs sb-box sb-outline" style="top:314px">Device Verification &amp;<br>Certification</div>
  <div class="abs sb-box sb-filled" style="top:366px">Attack &amp; Behaviours<br>Simulators</div>
  <div class="abs sandbox-frame"></div>
  <div class="abs sb-box sb-filled" style="top:421px">Automated Cyber security<br>Certification</div>
  <div class="abs sandbox-word">Sandbox</div>
  <div class="abs sandbox-env"><b>MORVAL</b><br>Sandbox Environment</div>

  <div class="abs platform">Common Integration Platform</div>
</body>
</html>
```